A clean crisp business card for a Landscape Construction company. Designed to be easy to read contact/ info and also be appealing/interesting, unlike a traditional business card.

Industry/Entity Type

Landscape Construction

Contact Information for Business Card

Company name : Bramblecrest Landscape Construction, phone number: (877) 62Vales, website:Bramblecrestlandscapes.example, Email, sales@bramblecrestlandscapes.example

Requirements
Nice to have
• Luxurious finishes/ details…. Icons or emblems next to contact info
Should not have
• Clipart or general pictures

```html
<!DOCTYPE html>
<html lang="en">
<head>
<meta charset="utf-8">
<title>Bramblecrest Landscape Construction – Business Card</title>
<link rel="stylesheet" href="https://fonts.googleapis.com/css2?family=Montserrat:wght@500&family=Arimo:wght@400&display=swap">
<style>
  :root {
    --ink: #111111;
    --brand-blue: #2a78e4;
    --brand-green: #7fd321;
    --leaf-blue: #3b7fe8;
    --leaf-teal: #3aa88e;
    --leaf-green: #86e02a;
    --meadow-top: #ffffff;
    --meadow-mid: #dcf5c4;
    --meadow-low: #9fe64e;
    --divider: #f2c9cf;
  }
  * { margin: 0; padding: 0; box-sizing: border-box; }
  html, body { width: 1200px; height: 750px; overflow: hidden; background: #ffffff; }
  .card {
    position: relative;
    width: 1200px;
    height: 750px;
    overflow: hidden;
    background: linear-gradient(180deg, var(--meadow-top) 0%, var(--meadow-top) 50%, var(--meadow-mid) 64%, var(--meadow-low) 100%);
    font-family: "Arimo", Arial, sans-serif;
    color: var(--ink);
  }
  .leaf-art {
    position: absolute;
    left: 0;
    top: 0;
    width: 340px;
    height: 750px;
    border-radius: 0 55% 55% 0 / 0 40% 40% 0;
    background: linear-gradient(180deg, var(--leaf-blue) 0%, var(--leaf-teal) 42%, var(--leaf-green) 100%);
  }
  .brand-corner {
    position: absolute;
    top: 38px;
    left: 877px;
    height: 156px;
    padding-left: 26px;
    border-left: 2px solid var(--divider);
    display: flex;
    align-items: center;
    gap: 14px;
  }
  .brand-corner__dot {
    width: 34px;
    height: 34px;
    border-radius: 50%;
    background: var(--brand-green);
    flex: none;
  }
  .brand-corner__name {
    font-family: "Arimo", Arial, sans-serif;
    font-weight: 400;
    color: var(--brand-blue);
    line-height: 1.1;
  }
  .brand-corner__title { display: block; font-size: 34px; }
  .brand-corner__sub { display: block; font-size: 14px; letter-spacing: 1.5px; text-transform: uppercase; }
  .person-name {
    position: absolute;
    left: 458px;
    top: 310px;
    font-family: "Montserrat", Arial, sans-serif;
    font-weight: 500;
    font-size: 37px;
    color: var(--ink);
  }
  .company {
    position: absolute;
    left: 468px;
    top: 452px;
    font-family: "Arimo", Arial, sans-serif;
    font-weight: 400;
    color: var(--ink);
    text-transform: uppercase;
    line-height: 1;
  }
  .company__name { display: block; font-size: 50px; letter-spacing: 1px; }
  .company__line { display: block; font-size: 19px; letter-spacing: 4.6px; margin-top: 6px; padding-top: 3px; border-top: 1.5px solid var(--ink); }
  .contact-list {
    position: absolute;
    left: 466px;
    top: 546px;
    list-style: none;
    font-size: 34px;
  }
  .contact-list li { display: flex; align-items: center; gap: 8px; height: 52px; }
  .contact-icon { width: 30px; height: 30px; flex: none; }
  .contact-icon--mail { width: 38px; }
</style>
</head>
<body>
  <main class="card">
    <div class="leaf-art" role="img" aria-label="Two large stylised leaves shading from blue to green"></div>

    <div class="brand-corner">
      <span class="brand-corner__dot"></span>
      <p class="brand-corner__name">
        <span class="brand-corner__title">Bramblecrest</span>
        <span class="brand-corner__sub">Landscape Construction</span>
      </p>
    </div>

    <h1 class="person-name">Your name Your name</h1>

    <p class="company">
      <span class="company__name">Bramblecrest</span>
      <span class="company__line">Landscape Construction</span>
    </p>

    <ul class="contact-list">
      <li>
        <svg class="contact-icon" viewBox="0 0 30 30" aria-hidden="true">
          <circle cx="15" cy="15" r="13" fill="none" stroke="#111" stroke-width="1.8"/>
          <path d="M10 8c1-1 2 0 3 2s0 2-1 3c1 2 2 3 4 4 1-1 1-2 3-1s3 2 2 3c-1 2-3 3-6 1-3-2-5-4-6-7-1-2 0-4 1-5z" fill="#111"/>
        </svg>
        <span>(877) 62Vales</span>
      </li>
      <li>
        <svg class="contact-icon" viewBox="0 0 30 30" aria-hidden="true">
          <g fill="none" stroke="#111" stroke-width="1.8">
            <circle cx="15" cy="15" r="13"/>
            <ellipse cx="15" cy="15" rx="6" ry="13"/>
            <path d="M2 15h26M4 8h22M4 22h22"/>
          </g>
        </svg>
        <span>Bramblecrestlandscapes.example</span>
      </li>
      <li>
        <svg class="contact-icon contact-icon--mail" viewBox="0 0 38 30" aria-hidden="true">
          <g fill="none" stroke="#111" stroke-width="1.8">
            <rect x="2" y="4" width="34" height="22"/>
            <path d="M2 4l17 13 17-13M2 26l13-11M36 26l-13-11"/>
          </g>
        </svg>
        <span>sales@bramblecrestlandscapes.example</span>
      </li>
    </ul>
  </main>
</body>
</html>
```